Business card for Luxury Portable Restroom Trailer company

We are a Luxury Portable Restroom Trailer Company Called PELIKAR HIRES. Based in Orange County California. We provide portable restroom trailers for events, such as, Weddings, Concerts, Charity events, Sporting events, Tournaments, Corporate events, ect. We rent and Sell the Luxury restrooms. Our colors are white, grey, and Orange. As you will see in the logo we uploaded.
There are 2 people in the company so the names and titles will change for the 3 people but card will remain the same. Here is the information for each Person: Dennis Moyle CFO 555 018-3647
next Person: Wesley Tanford VP 555 018-3647
Next Person: Miles Tanford CEO 555 018-3647
Information to include on the card: Luxury Restroom Trailers Rental and Sales. Weddings, Concerts, Charity, Sporting and Corp. Events.

```html
<!DOCTYPE html>
<html lang="en">
<head>
<meta charset="utf-8">
<title>PELIKAR HIRES – Business Card</title>
<link href="https://fonts.googleapis.com/css2?family=Montserrat:wght@400;500;700&display=swap" rel="stylesheet">
<style>
  :root {
    --orange: #f26a21;
    --card-white: #ffffff;
    --card-black: #141414;
    --pattern-black: #1d1d1d;
    --ink: #2b2b2b;
    --grey: #6b6b6b;
    --stage: #1f1f22;
  }
  * { box-sizing: border-box; margin: 0; padding: 0; }
  html, body {
    width: 1200px; height: 900px; overflow: hidden;
    background: var(--stage);
    font-family: "Montserrat", Arial, sans-serif;
  }
  .canvas { position: relative; width: 1200px; height: 900px; }
  .card {
    position: absolute; left: 280px;
    width: 640px; height: 366px;
    border-radius: 22px; overflow: hidden;
  }
  .card-back { top: 59px; background: var(--card-black); }
  .card-front { top: 475px; background: var(--card-white); }

  .back-pattern {
    position: absolute; inset: 0;
    background: radial-gradient(circle at 60% 40%, var(--pattern-black), var(--card-black) 75%);
  }
  .back-badge {
    position: absolute; left: 430px; top: 96px;
    width: 40px; height: 40px; border-radius: 50%;
    border: 3px solid var(--orange);
  }

  .hero-ring {
    position: absolute; left: 360px; top: -30px;
    width: 426px; height: 426px; border-radius: 50%;
    border: 18px solid var(--orange);
  }
  .services {
    position: absolute; left: 420px; top: 128px; width: 196px;
    color: var(--ink);
  }
  .services-headline {
    font-weight: 700; font-size: 15px; line-height: 1.3; color: var(--orange);
  }
  .services-events {
    margin-top: 10px; font-weight: 500; font-size: 12px; line-height: 1.45; color: var(--grey);
  }
  .brand {
    position: absolute; left: 40px; top: 96px;
    font-weight: 700; font-size: 26px; letter-spacing: 1px;
    color: var(--orange);
  }
  .person { position: absolute; left: 40px; top: 160px; }
  .person-name {
    font-weight: 700; font-size: 26px; color: var(--orange); line-height: 1.1;
  }
  .person-title {
    font-weight: 400; font-size: 15px; color: var(--ink); margin-top: 2px;
  }
  .address {
    position: absolute; left: 40px; top: 226px;
    font-size: 13px; line-height: 1.3; color: var(--ink);
  }
  .contacts {
    position: absolute; left: 40px; top: 268px; list-style: none;
    font-size: 13px; color: var(--ink); line-height: 1.3;
  }
  .contacts li { display: flex; align-items: center; gap: 8px; height: 19px; }
  .contacts svg { width: 12px; height: 12px; fill: var(--orange); flex: none; }
</style>
</head>
<body>
<main class="canvas">
  <section class="card card-back">
    <div class="back-pattern" role="img" aria-label="Tone-on-tone embossed brand pattern in black"></div>
    <div class="back-badge"></div>
  </section>

  <section class="card card-front">
    <div class="hero-ring"></div>
    <div class="services">
      <p class="services-headline">Luxury Restroom Trailers<br>Rental and Sales</p>
      <p class="services-events">Weddings, Concerts, Charity, Sporting and Corp. Events</p>
    </div>
    <div class="brand">PELIKAR HIRES</div>
    <div class="person">
      <div class="person-name">Miles Tanford</div>
      <div class="person-title">CEO</div>
    </div>
    <p class="address">418 Harbor Crest Ave. #112<br>Costa Mesa, CA 92626</p>
    <ul class="contacts">
      <li><svg viewBox="0 0 24 24"><path d="M6.6 10.8a15 15 0 0 0 6.6 6.6l2.2-2.2a1 1 0 0 1 1-.25 11.4 11.4 0 0 0 3.6.57 1 1 0 0 1 1 1V20a1 1 0 0 1-1 1A17 17 0 0 1 3 4a1 1 0 0 1 1-1h3.5a1 1 0 0 1 1 1c0 1.25.2 2.45.57 3.57a1 1 0 0 1-.25 1z"/></svg>555 018-3647</li>
      <li><svg viewBox="0 0 24 24"><path d="M7 1h10a2 2 0 0 1 2 2v18a2 2 0 0 1-2 2H7a2 2 0 0 1-2-2V3a2 2 0 0 1 2-2zm0 3v14h10V4zm5 15.5a1 1 0 1 0 0 2 1 1 0 0 0 0-2z"/></svg>555 018-3647</li>
      <li><svg viewBox="0 0 24 24"><path d="M2 5h20v14H2zm2 2v.5l8 5 8-5V7z"/></svg>info@pelikarhires.com</li>
      <li><svg viewBox="0 0 24 24"><path d="M12 2a10 10 0 1 0 0 20 10 10 0 0 0 0-20zm6.9 9h-3a15 15 0 0 0-1.4-6A8 8 0 0 1 18.9 11zM12 4.1c.9 1.3 1.7 3.6 1.9 6.9h-3.8c.2-3.3 1-5.6 1.9-6.9zM9.5 5a15 15 0 0 0-1.4 6h-3A8 8 0 0 1 9.5 5zm-4.4 8h3a15 15 0 0 0 1.4 6 8 8 0 0 1-4.4-6zm6.9 6.9c-.9-1.3-1.7-3.6-1.9-6.9h3.8c-.2 3.3-1 5.6-1.9 6.9zm2.5-.9a15 15 0 0 0 1.4-6h3a8 8 0 0 1-4.4 6z"/></svg>www.pelikarhires.com</li>
    </ul>
  </section>
</main>
</body>
</html>
```